Piano genealogy graphs template, for a large poster printing

Hello and thank you for your interest in my project.
I need a poster template, so I can create structures similar to the one I have uploaded. I want to completely replace or improve my poor previous design which is attached.
I need to be able to input names and dates into boxes of various colors, arrows pointing between boxes. I would also like to be able to label each graph (not each box).
I am looking at something that would be legible when printed, in a one consistent professional layout of 2A0 (around 1189x1682 mm) poster (I know it is large). The design template required here can include just few sample text boxes with sample flags on a suitable background, for me to multiply later and spread across the whole poster.
The positioning of the boxes is not important.
Please let me know if more clarification is required.
Thank you for your help.

Feel free to follow what I have attached in the file, or change the design completely.

UPDATE 4/12: I have uploaded two more graphs as an example. At this stage of the contest, I would like to have one of those graphs done, and I am planning to offer a 'freelance job' to one or two designers, who will be willing to do the whole 10 graphs on one poster.
Updates

Reason: Dear Designers, Since the project is rather complex and large-scale, I have decided to give everyone more time to work on their designs. I will consider extending it further if any of you require additional time. Best wishes, bronisław

Dear Designers, I would like to inform you that the contest for my poster is now closed and that I have assigned the prizes. I would like to thank all of you for submiting your high-quality designs, and for your participation. It was a great pleasure working with all of you. Due to the large size of the project itself (large number of graphs to be fitted on a single poster), I had to focus on providing feedback to only those designers who provided projects closest to what I was expecting at the early stages of the contest. I wish you all the best for the future, Kind regards, Bronisław

Target Market(s)

Pianists, historians

Industry/Entity Type

Printing

Requirements
Must have
• Consistent design, but allow to clearly delineate various genealogy trees.

```html
<!DOCTYPE html>
<html lang="en">
<head>
<meta charset="utf-8">
<title>Genealogical Trees of Pianists – French Tree</title>
<link rel="stylesheet" href="https://fonts.googleapis.com/css2?family=Tinos:ital,wght@0,400;0,700;1,400;1,700&display=swap">
<style>
:root{
  --page:#f1eedb;
  --panel:#e3d088;
  --header:#dccb86;
  --footer-band:#d3bf72;
  --ink:#2f2418;
  --line:#3a2a1c;
  --hash:#d0382b;
  --bullet:#1f8a3b;
  --ghost:#c9b063;
  --map:#d2bd72;
}
*{margin:0;padding:0;box-sizing:border-box}
html,body{width:900px;height:1200px;overflow:hidden;background:var(--page)}
body{font-family:"Tinos",serif;color:var(--ink)}
.canvas{position:relative;width:900px;height:1200px}
.poster{position:absolute;left:115px;top:12px;width:672px;height:1165px;background:var(--panel)}
.poster-header{position:absolute;left:115px;top:12px;width:672px;height:78px;background:var(--header)}
.poster-title{position:absolute;left:115px;top:60px;width:672px;text-align:center;font-size:21px;font-weight:400;font-variant:small-caps;letter-spacing:.5px;color:var(--ink)}
.rule{position:absolute;left:115px;width:672px;background:var(--line)}
.rule.a{top:89px;height:2px}
.rule.b{top:94px;height:1px}
.keyboard{position:absolute;left:115px;top:97px;width:672px;height:84px;background:linear-gradient(180deg,#f6efd8,#ece2c4)}
.keyboard-edge{position:absolute;left:115px;top:181px;width:672px;height:5px;background:#d6c275}
.map-area{position:absolute;left:275px;top:410px;width:370px;height:480px;border-radius:40% 30% 35% 45%;background:radial-gradient(ellipse at center,var(--map),rgba(210,189,114,.35) 75%,rgba(210,189,114,0) 100%)}
.piano-area{position:absolute;left:572px;top:905px;width:150px;height:135px;border-radius:40% 50% 8% 8%;background:linear-gradient(180deg,#d8c47c,#d2bd72)}
.piano-icon{position:absolute;left:426px;top:1030px;width:38px;height:20px;border-radius:45% 55% 3px 3px;background:var(--line)}
.tree-label{position:absolute;left:152px;top:945px;width:215px;color:var(--ghost);font-weight:700}
.tree-label .big{display:block;font-size:51px;letter-spacing:2px;line-height:52px;font-variant:small-caps}
.tree-label .small{display:block;text-align:right;font-size:22px;letter-spacing:2px;line-height:22px;font-variant:small-caps}
.connectors{position:absolute;left:0;top:0}
.family{position:absolute;transform:translateX(-50%);text-align:center;white-space:nowrap;font-size:10px;line-height:12px}
.students li{list-style:none}
.bullet{display:inline-block;width:5px;height:5px;border-radius:50%;background:var(--bullet);margin-right:4px;vertical-align:1px}
.mark{color:var(--hash);font-size:10px;line-height:12px}
.teacher{margin-top:3px;font-weight:700;font-size:10px;line-height:12px}
.flag{display:inline-block;width:13px;height:8px;margin-left:3px;vertical-align:-1px}
.us{background:linear-gradient(90deg,#2d4590 0 45%,transparent 45%),repeating-linear-gradient(180deg,#c8312f 0 1.15px,#fff 1.15px 2.3px)}
.uk{background:linear-gradient(90deg,transparent 42%,#c8312f 42% 58%,transparent 58%),linear-gradient(180deg,transparent 38%,#c8312f 38% 62%,transparent 62%),#24367a}
.nz{background:linear-gradient(90deg,#2a3f8c 0 50%,#243578 50%)}
.tn{background:#d2242a}
.it{background:linear-gradient(90deg,#1f9a4a 0 33%,#fff 33% 66%,#cf2b2b 66%)}
.ro{background:linear-gradient(90deg,#1f3b8f 0 33%,#f5cd1e 33% 66%,#cf2b2b 66%)}
.be{background:linear-gradient(90deg,#111 0 33%,#f5d11e 33% 66%,#cf2b2b 66%)}
.gr{background:repeating-linear-gradient(180deg,#2d63b4 0 .9px,#fff .9px 1.8px)}
.pl{background:linear-gradient(180deg,#fff 0 50%,#d4213d 50%)}
.br{background:#1f9a4a;box-shadow:inset 0 0 0 2px #1f9a4a,inset 0 0 0 4px #f5d11e}
.ru{background:linear-gradient(180deg,#fff 0 33%,#2d4fa8 33% 66%,#cf2b2b 66%)}
.ch{background:#d2242a}
.bg{background:linear-gradient(180deg,#fff 0 33%,#1f9a4a 33% 66%,#cf2b2b 66%)}
.de{background:linear-gradient(180deg,#111 0 33%,#cf2b2b 33% 66%,#f5cd1e 66%)}
.footer-band{position:absolute;left:115px;top:1060px;width:672px;height:117px;background:var(--footer-band)}
.legend{position:absolute;left:152px;top:1079px;font-size:10px;line-height:16px;font-style:italic;font-weight:700}
.legend .mark{display:inline-block;width:9px;font-style:normal}
.legend .bullet{margin-right:14px}
.footer-caption{position:absolute;left:115px;top:1148px;width:672px;text-align:center;font-size:10px}
</style>
</head>
<body>
<div class="canvas">
  <div class="poster"></div>
  <div class="poster-header"></div>
  <h1 class="poster-title">Genealogical Trees of Pianists</h1>
  <div class="rule a"></div><div class="rule b"></div>
  <div class="keyboard" role="img" aria-label="Piano keyboard band with black and white keys"></div>
  <div class="keyboard-edge"></div>

  <div class="map-area" role="img" aria-label="Faint map silhouette of France"></div>
  <div class="piano-area" role="img" aria-label="Faint grand piano silhouette"></div>

  <div class="tree-label"><span class="big">French</span><span class="small">Tree</span></div>

  <svg class="connectors" width="900" height="1200" viewBox="0 0 900 1200" aria-hidden="true">
    <g stroke="var(--line)" stroke-width="2" fill="none">
      <path d="M293 340V368H448V340M368 368V478"/>
      <path d="M599 300V335M599 418V566"/>
      <path d="M212 540V566H678V540M368 497V566M514 540V566M445 566V590"/>
      <path d="M237 716V744H652V716M445 716V770"/>
      <path d="M237 878V907H652V878M445 878V930M445 963V990"/>
    </g>
    <g fill="var(--line)">
      <circle cx="293" cy="340" r="2.5"/><circle cx="448" cy="340" r="2.5"/>
      <circle cx="599" cy="300" r="2.5"/><circle cx="599" cy="418" r="2.5"/>
      <circle cx="212" cy="540" r="2.5"/><circle cx="368" cy="497" r="2.5"/>
      <circle cx="514" cy="540" r="2.5"/><circle cx="678" cy="540" r="2.5"/>
      <circle cx="237" cy="716" r="2.5"/><circle cx="445" cy="716" r="2.5"/><circle cx="652" cy="716" r="2.5"/>
      <circle cx="237" cy="878" r="2.5"/><circle cx="445" cy="878" r="2.5"/><circle cx="652" cy="878" r="2.5"/>
      <circle cx="445" cy="963" r="2.5"/>
    </g>
  </svg>

  <section class="family" style="left:293px;top:262px">
    <ul class="students">
      <li>Lionel Marchetti (1946)</li>
      <li>Gérard Fonteneau (1949)</li>
      <li>Bernard Quillet (1943)</li>
    </ul>
    <div class="mark">#</div>
    <div class="teacher">Henri Valmont<br>(1914-2005)</div>
  </section>

  <section class="family" style="left:448px;top:250px">
    <ul class="students">
      <li>Sylvain Archambault (1963)</li>
      <li>Odile Ferrandon (1954)</li>
      <li>Thierry Bonnal (1952)</li>
      <li>Agnès Ferrandon (1949)</li>
    </ul>
    <div class="mark">#</div>
    <div class="teacher">Simone Pradier<br>(1908)</div>
  </section>

  <section class="family" style="left:599px;top:202px">
    <ul class="students">
      <li><span class="bullet"></span>Daniel Whitcombe (1971)<span class="flag us"></span></li>
      <li>Olivier Castaing (1958)</li>
      <li><span class="bullet"></span>Graham Pennock (1955)<span class="flag uk"></span></li>
      <li>Rémi Dautrey (1951)</li>
      <li><span class="bullet"></span>Stuart Fenwick (1946)<span class="flag uk"></span></li>
    </ul>
    <div class="mark">#</div>
    <div class="teacher">Hélène Morvan<br>(1925-2011)</div>
  </section>

  <section class="family" style="left:599px;top:332px">
    <ul class="students">
      <li><span class="bullet"></span>Karim Belhadj (1959)<span class="flag tn"></span></li>
      <li>Josette Cabanel (1937)</li>
      <li><span class="bullet"></span>Martin Ashworth (1931)<span class="flag nz"></span></li>
      <li><span class="bullet"></span>Miriam Holloway (1921-1983)<span class="flag us"></span></li>
    </ul>
    <div class="mark">#</div>
    <div class="teacher">Gaston Revel<br>(1889-1978)</div>
  </section>

  <section class="family" style="left:212px;top:393px">
    <ul class="students">
      <li><span class="bullet"></span>Paolo Ferrante (1942-1976)<span class="flag it"></span></li>
      <li>Lucien Marais (1935)</li>
      <li><span class="bullet"></span>Daniel Kessler (1931)<span class="flag us"></span></li>
      <li><span class="bullet"></span>Helen Brandvold (1926)<span class="flag us"></span></li>
      <li><span class="bullet"></span>Mihai Dobrescu (1916-1952)<span class="flag ro"></span></li>
      <li><span class="bullet"></span>Eleni Katsarou (1911-1978)<span class="flag gr"></span></li>
      <li><span class="bullet"></span>Tadeusz Wierzbicki (1905-1999)<span class="flag pl"></span></li>
      <li>Odette Lambrecht (1897-1984)</li>
      <li><span class="bullet"></span>Lúcia Mendonça (1894-1983)<span class="flag br"></span></li>
    </ul>
    <div class="mark">#</div>
    <div class="teacher"><span class="bullet"></span>Émile Jorand<span class="flag ch"></span><br>(1876-1960)</div>
  </section>

  <section class="family" style="left:368px;top:466px">
    <div class="teacher">Léon Audran<br>(1889-1957)</div>
  </section>

  <section class="family" style="left:514px;top:450px">
    <ul class="students">
      <li><span class="bullet"></span>Selin Aydemir (1943)<span class="flag tn"></span></li>
      <li><span class="bullet"></span>Rafael Teixeira (1939)<span class="flag br"></span></li>
      <li>Claude Vernier (1937)</li>
      <li>Bernard Lasalle (1933)</li>
    </ul>
    <div class="mark">#</div>
    <div class="teacher">André Fauvel<br>(1905-1984)</div>
  </section>

  <section class="family" style="left:678px;top:450px">
    <ul class="students">
      <li><span class="bullet"></span>Nikolai Varensky (1911-1974)<span class="flag ru"></span></li>
      <li>Denise Mauclair (1908-1989)</li>
      <li><span class="bullet"></span>Arthur Pendleton (1903-1986)<span class="flag uk"></span></li>
      <li><span class="bullet"></span>Elena Vasilescu (1896-1962)<span class="flag ro"></span></li>
    </ul>
    <div class="mark">#</div>
    <div class="teacher"><span class="bullet"></span>Maurice Duchêne<span class="flag be"></span><br>(1880-1961)</div>
  </section>

  <section class="family" style="left:237px;top:603px">
    <ul class="students">
      <li>Roland Bessière (1925-1972)</li>
      <li>Françoise Aubert-Rolland (1922-2003)</li>
      <li>Jeanne Dufresnoy (1919-1990)</li>
      <li><span class="bullet"></span>Harold Prescott (1916-2008)<span class="flag us"></span></li>
      <li>Hélène Chabrier (1903-1997)</li>
      <li>Paul Desmarais (1899-1981)</li>
    </ul>
    <div class="mark">#</div>
    <div class="teacher">Adèle Thibault<br>(1864-1921)</div>
  </section>

  <section class="family" style="left:445px;top:591px">
    <ul class="students">
      <li>Hélène Chabrier (1903-1997)</li>
      <li>Gustave Chabrier(1897-1974)</li>
      <li>E. Victor Lemoine(1888-1951)</li>
      <li>Albert Rouchon (1885-1969)</li>
      <li><span class="bullet"></span>Umberto Saletti (1881-1949)<span class="flag it"></span></li>
      <li><span class="bullet"></span>Konrad Hessler (1871-1931)<span class="flag de"></span></li>
      <li><span class="bullet"></span>Stanisław Wróblak (1868-1944)<span class="flag pl"></span></li>
    </ul>
    <div class="mark">#</div>
    <div class="teacher">Auguste Ravenel<br>(1841-1917)</div>
  </section>

  <section class="family" style="left:652px;top:591px">
    <ul class="students">
      <li><span class="bullet"></span>Daniel Kessler (1931)<span class="flag us"></span></li>
      <li><span class="bullet"></span>Boris Stoyanov (1928)<span class="flag bg"></span></li>
      <li><span class="bullet"></span>Leonard Ashby (1924-1990)<span class="flag us"></span></li>
      <li><span class="bullet"></span>Graeme Fullerton (1921-1955)<span class="flag nz"></span></li>
      <li><span class="bullet"></span>Walter Brockman (1920-1954)<span class="flag us"></span></li>
      <li><span class="bullet"></span>Edwin Marsh (1917-1986)<span class="flag us"></span></li>
      <li><span class="bullet"></span>Dorothy Whitfield (1913-2001)<span class="flag us"></span></li>
    </ul>
    <div class="mark">#</div>
    <div class="teacher"><span class="bullet"></span>Vera Lindgren<span class="flag us"></span><br>(1880-1950)</div>
  </section>

  <section class="family" style="left:445px;top:769px">
    <ul class="students">
      <li>Gabriel Lucet (1863-1920)</li>
      <li>Étienne Morlaix (1850-1929)</li>
      <li>Alexandre Daubray (1849-1905)</li>
      <li>Jules Fromentin (1844-1909)</li>
      <li>Édouard Latour (1837-1932)</li>
      <li>Camille Rosier (1840-1877)</li>
    </ul>
    <div class="mark">#</div>
    <div class="teacher">Jean-Baptiste Lambrière<br>(1820-1888)</div>
  </section>

  <section class="family" style="left:237px;top:850px">
    <div class="teacher">Charles-Henri Valcourt<br>(1815-1886)</div>
  </section>

  <section class="family" style="left:652px;top:850px">
    <div class="teacher"><span class="bullet"></span>Henri Vermeulen<span class="flag be"></span><br>(1824-1892)</div>
  </section>

  <section class="family" style="left:445px;top:931px">
    <div class="teacher">Louis Garnerin<br>(1787 - 1855)</div>
  </section>

  <section class="family" style="left:445px;top:991px">
    <div class="teacher">Jean-Antoine Pellissier<br>(1773 - 1836)</div>
  </section>

  <div class="piano-icon" role="img" aria-label="Small grand piano icon"></div>

  <div class="footer-band"></div>
  <div class="legend">
    <p><span class="bullet"></span>Indicates People born in the respective country flag shown. All others were born in France.</p>
    <p><span class="mark">#</span>&nbsp;&nbsp;&nbsp;Indicates the students of the below personal.</p>
  </div>
  <p class="footer-caption">Genealogical Trees of Pianists - French Tree</p>
</div>
</body>
</html>
```